Coding for One Page Website

Website was previously designed using Craftmeadow (attached). I now need it coded so I can publish using Webtulip.

Company: Amber Ridge Funds

Reason: Still waiting for exactly what I need.

Industry/Entity Type

It Company

```html
<!DOCTYPE html>
<html lang="en">
<head>
<meta charset="utf-8">
<title>Amber Ridge Funds</title>
<link href="https://fonts.googleapis.com/css2?family=Open+Sans:wght@400;600;700&display=swap" rel="stylesheet">
<style>
:root{
  --white:#ffffff;
  --band:#f0f0f0;
  --ink:#222222;
  --muted:#6b6b6b;
  --link:#1a73c9;
  --accent:#1b7fd6;
  --footer:#0a5291;
  --footer-bar:#1572cf;
  --field-border:#c9d6e3;
  --teal:#1f8c8c;
  --red:#d6333a;
  --orange:#f08a24;
}
*{margin:0;padding:0;box-sizing:border-box}
html,body{width:1200px;height:656px;overflow:hidden;background:var(--white)}
body{position:relative;font-family:"Open Sans",Arial,sans-serif;color:var(--ink)}
.abs{position:absolute}

.hero-button{left:574px;top:0;width:52px;height:6px;background:var(--accent);border-radius:0 0 3px 3px}
.hero-art{left:546px;top:18px;width:108px;height:78px;border-radius:6px;
  background:linear-gradient(180deg,#dfe6ee 0%,#b9c7d4 55%,#c79a62 100%)}

.services{left:0;top:139px;width:1200px;height:249px;background:var(--band)}
.section-title{width:1200px;left:0;text-align:center;font-size:7.5px;font-weight:600;letter-spacing:.3px;text-transform:uppercase;line-height:10px}
.services .section-title{top:7px}
.service{top:22px;width:323px}
.service-photo{height:174px}
.service-title{margin-top:6px;font-size:7.5px;line-height:9.6px;color:var(--link);font-weight:400}
.service-text{margin-top:6px;font-size:7px;line-height:9.6px;color:var(--muted)}
.photo-retail{background:linear-gradient(135deg,#9fb3d8,#3e4450 60%,#b7c3de)}
.photo-terminal{background:linear-gradient(135deg,#e9ecef,#a7acb2 55%,#d9c4b0)}
.photo-mobile{background:linear-gradient(135deg,#cfd8c0,#4b5a6b 55%,#9b7a60)}

.applications .section-title{top:427px}
.app{display:flex;align-items:center;gap:7px;font-size:6.5px;color:var(--ink)}
.app svg{width:18px;height:18px;flex:none}

.footer-line{left:0;top:524px;width:1200px;height:6px;background:var(--accent)}
.footer{left:0;top:530px;width:1200px;height:106px;background:var(--footer);color:var(--white)}
.footer-heading{font-size:7px;font-weight:700;text-transform:uppercase;line-height:9px}
.footer-links{list-style:none;margin-top:10px;font-size:7px;font-weight:600;line-height:9.6px}
.footer-note{left:80px;top:84px;font-size:7px;font-weight:600}
.field{background:var(--white);border:1px solid var(--field-border);font-size:6.5px;color:#777;padding:2px 3px;line-height:12px}
.send{left:976px;top:92px;width:52px;height:12px;background:var(--footer-bar);font-size:6.5px;text-align:center;line-height:12px;color:var(--white);border-bottom:1px solid #7fb4e6}
.copyright{left:0;top:636px;width:1200px;height:20px;background:var(--footer-bar);color:var(--white);font-size:7px;font-weight:600;text-align:center;line-height:20px}
</style>
</head>
<body>

<header>
  <div class="abs hero-button"></div>
  <div class="abs hero-art" role="img" aria-label="Illustration of a desktop computer on a desk with hands holding cards and a phone above the screen"></div>
</header>

<section class="abs services">
  <h2 class="abs section-title">We make payments easy</h2>
  <article class="abs service" style="left:80px">
    <div class="service-photo photo-retail" role="img" aria-label="Photo of a hand inserting a card into a wireless card machine"></div>
    <p class="service-title">Retail<br>Wired &amp; Wireless Machines</p>
    <p class="service-text">Lorem Ipsum is simply dummy text of the printing and typesetting industry. Lorem Ipsum has been the industry's standard dummy text ever since the 1500s.</p>
  </article>
  <article class="abs service" style="left:439px">
    <div class="service-photo photo-terminal" role="img" aria-label="Photo of hands holding a card while typing on a laptop"></div>
    <p class="service-title">Virtual Terminal<br>Payments on your Computer or Website</p>
    <p class="service-text">Lorem Ipsum is simply dummy text of the printing and typesetting industry. Lorem Ipsum has been the industry's standard dummy text ever since the 1500s.</p>
  </article>
  <article class="abs service" style="left:797px">
    <div class="service-photo photo-mobile" role="img" aria-label="Photo of a card swiped through a reader attached to a smartphone"></div>
    <p class="service-title">Mobile<br>Smartphones &amp; Tablets</p>
    <p class="service-text">Lorem Ipsum is simply dummy text of the printing and typesetting industry. Lorem Ipsum has been the industry's standard dummy text ever since the 1500s.</p>
  </article>
</section>

<section class="applications">
  <h2 class="abs section-title">Amber Ridge Funds across multiple applications</h2>
  <div class="abs app" style="left:458px;top:446px">
    <svg viewBox="0 0 18 18"><rect x="2" y="3" width="14" height="12" rx="1" fill="var(--teal)"/><rect x="4" y="5" width="10" height="3" fill="#fff"/></svg>For point of sale</div>
  <div class="abs app" style="left:560px;top:446px">
    <svg viewBox="0 0 18 18"><rect x="1" y="5" width="12" height="9" rx="1" fill="var(--accent)"/><rect x="7" y="2" width="10" height="7" rx="1" fill="var(--orange)"/></svg>For payment</div>
  <div class="abs app" style="left:652px;top:446px">
    <svg viewBox="0 0 18 18"><circle cx="9" cy="9" r="8" fill="var(--accent)"/><rect x="6" y="4" width="6" height="10" rx="1" fill="#fff"/></svg>For self service</div>
  <div class="abs app" style="left:458px;top:477px">
    <svg viewBox="0 0 18 18"><rect x="2" y="3" width="14" height="11" rx="1" fill="none" stroke="var(--red)" stroke-width="2"/><rect x="7" y="14" width="4" height="2" fill="var(--red)"/></svg>For digital signage</div>
  <div class="abs app" style="left:562px;top:477px">
    <svg viewBox="0 0 18 18"><rect x="5" y="1" width="8" height="16" rx="1.5" fill="var(--teal)"/><rect x="6.5" y="3" width="5" height="10" fill="#fff"/></svg>For mobility</div>
  <div class="abs app" style="left:650px;top:477px">
    <svg viewBox="0 0 18 18"><circle cx="9" cy="9" r="8" fill="var(--orange)"/><path d="M4 9h10M10 5l4 4-4 4" stroke="var(--accent)" stroke-width="2" fill="none"/></svg>For warehouse &amp; distribution</div>
</section>

<div class="abs footer-line"></div>
<footer class="abs footer">
  <div class="abs" style="left:80px;top:12px">
    <h3 class="footer-heading">Quick Links</h3>
    <ul class="footer-links"><li>&gt; Home</li><li>&gt; About Us</li><li>&gt; Program</li><li>&gt; Products</li><li>&gt; Contact Us</li></ul>
  </div>
  <div class="abs" style="left:389px;top:12px">
    <h3 class="footer-heading">Business Overview</h3>
    <ul class="footer-links"><li>&gt; Testimonial</li><li>&gt; Event and News</li><li>&gt; Careers</li><li>&gt; Honors &amp; Awards</li><li>&gt; Q&amp;A</li></ul>
  </div>
  <p class="abs footer-note">Amber Ridge Funds is a registered MSP/ISO of the Canadian branch of Northbay Trust Association and Corvane.</p>
  <h3 class="abs footer-heading" style="left:976px;top:12px">Contact Us</h3>
  <div class="abs field" style="left:976px;top:23px;width:159px;height:17px">Name</div>
  <div class="abs field" style="left:976px;top:47px;width:78px;height:17px">Email</div>
  <div class="abs field" style="left:1057px;top:47px;width:78px;height:17px">Phone</div>
  <div class="abs field" style="left:976px;top:69px;width:159px;height:19px;border:2px solid #333">Message</div>
  <div class="abs send">Send</div>
</footer>
<div class="abs copyright">Copyright © 2015 (Amber Ridge Funds) | All Rights Reserved</div>

</body>
</html>
```